Harwick Construction LTD is in need of a web page we are renovation and maintenance specialists

We are a medium size building company specialising in renovations and maintainance on commercial and residential properties bathrooms, kitchens, alterations, commercial shop fit outs, office fit outs. we also specialise in project management taking care of all manners of trades from concept to completion with trade qualified LBP registered builders customers can be assured that they will get the best possible results

Industry/Entity Type

Building

Coding

Coded - Design and coding required

Number of Pages Required

2 page

```html
<!DOCTYPE html>
<html lang="en">
<head>
<meta charset="utf-8">
<title>Harwick Construction LTD</title>
<link href="https://fonts.googleapis.com/css2?family=Open+Sans:wght@400;600;700;800&display=swap" rel="stylesheet">
<style>
:root{
  --ink:#2b2b2b;
  --muted:#777;
  --navy:#1d2c4c;
  --accent:#1f6fb9;
  --nav:#2a2a2a;
  --band:#3b3b3b;
  --footer:#2d2d2d;
  --footer-deep:#222;
  --line:#dcdcdc;
  --white:#fff;
}
*{box-sizing:border-box;margin:0;padding:0}
html,body{width:1200px;height:2348px;overflow:hidden}
body{position:relative;background:var(--white);font-family:"Open Sans",Arial,sans-serif;color:var(--ink)}
.abs{position:absolute}

/* header */
.topbar{left:0;top:0;width:1200px;height:88px;background:var(--white)}
.brand{left:220px;top:30px;display:flex;align-items:center;gap:10px}
.brand-square{width:12px;height:12px;background:var(--navy);flex:none}
.brand-name{font-weight:700;font-size:22px;color:var(--navy);line-height:1.2;white-space:nowrap}
.info{top:22px;display:flex;align-items:center;gap:8px;font-size:12px;color:#444;line-height:1.3}
.info svg{flex:none}
.social{top:26px;left:960px;display:flex;gap:10px}
.social span{width:18px;height:18px;border-radius:50%;background:#c7c7c7;display:block}

.nav{left:0;top:88px;width:1200px;height:48px;background:var(--nav)}
.nav ul{position:absolute;left:220px;top:0;display:flex;list-style:none;height:48px;align-items:center}
.nav li{font-size:12px;font-weight:700;color:#ddd;padding:0 18px;height:48px;line-height:48px}
.nav li.active{background:#3c3c3c;color:var(--white)}
.dropdown{left:428px;top:136px;width:172px;background:var(--white);box-shadow:0 2px 8px rgba(0,0,0,.25);z-index:3}
.dropdown div{font-size:12px;padding:10px 14px;border-bottom:1px solid var(--line);color:#333}

/* hero */
.hero{left:0;top:136px;width:1200px;height:384px;background:linear-gradient(120deg,#eef0f0 0%,#cfd5d6 40%,#a8b0b4 70%,#d9dcdc 100%)}
.hero-box{left:220px;top:266px;width:380px;padding:20px 22px;background:rgba(28,36,52,.82);color:var(--white);font-size:22px;font-weight:600;line-height:1.35}
.quote-bar{left:220px;top:528px;width:860px;height:56px;background:var(--navy);color:var(--white)}
.quote-bar p{position:absolute;left:28px;top:18px;font-size:14px;font-weight:600}
.btn-quote{right:16px;top:13px;background:var(--white);color:var(--navy);font-size:11px;font-weight:700;padding:8px 14px}

/* section heads */
.section-title{font-size:26px;font-weight:700;color:var(--ink)}
.section-title:after{content:"";display:block;width:56px;height:3px;background:var(--ink);margin-top:8px}
.arrows{display:flex;gap:4px}
.arrows span{width:26px;height:26px;background:#999;display:flex;align-items:center;justify-content:center}
.arrows span.on{background:var(--navy)}

/* services */
.card{top:668px;width:266px}
.card .img{width:266px;height:172px}
.card h3{font-size:13px;font-weight:700;margin-top:16px;color:var(--ink)}
.card p{font-size:11px;color:var(--muted);line-height:1.6;margin-top:8px}
.read{display:flex;align-items:center;gap:6px;font-size:11px;font-weight:700;margin-top:14px}
.read i{width:12px;height:12px;background:var(--ink);display:block}

/* featured */
.featured{left:0;top:1000px;width:1200px;height:360px;background:var(--band)}
.featured .section-title{color:var(--white)}
.featured .section-title:after{background:var(--white)}
.tabs{right:176px;top:52px;display:flex;gap:4px}
.tabs span{font-size:10px;font-weight:700;color:#ccc;padding:6px 10px}
.tabs span.on{background:var(--white);color:var(--ink)}
.tile{top:132px;width:200px;height:180px}
.tile-label{left:10px;bottom:52px;color:var(--white);font-weight:700;font-size:15px}
.tile-btn{left:10px;bottom:14px;background:var(--navy);color:var(--white);font-size:10px;font-weight:700;padding:8px 12px}
.side-arrow{top:206px;width:32px;height:32px;background:rgba(255,255,255,.15);display:flex;align-items:center;justify-content:center}

/* mission */
.mission{left:0;top:1360px;width:1200px;height:340px;background:linear-gradient(90deg,#c9d5dd 0%,#a9bac6 45%,#7c8d97 75%,#4e5b63 100%)}
.mission p{position:absolute;left:176px;top:70px;width:520px;font-size:24px;font-weight:700;color:#1f5c9c;line-height:1.35}

/* news */
.news{top:1784px;width:264px}
.news .img{width:264px;height:128px}
.news p{font-size:11px;color:var(--muted);line-height:1.6;margin-top:14px}
.news-meta{display:flex;justify-content:space-between;align-items:center;margin-top:18px}
.btn-dark{background:var(--navy);color:var(--white);font-size:11px;font-weight:700;padding:8px 14px}
.date{font-size:10px;color:var(--muted)}
.testi{left:768px;top:1784px;width:264px}
.testi-box{border:1px solid var(--line);padding:18px;font-size:11px;color:var(--muted);line-height:1.6;height:150px}
.testi-person{display:flex;align-items:center;gap:12px;margin-top:22px}
.avatar{width:54px;height:54px;background:linear-gradient(#8d98a3,#56606a)}
.testi-person b{font-size:11px;display:block}
.testi-person small{font-size:10px;color:var(--muted)}

/* footer */
.footer{left:0;top:2080px;width:1200px;height:232px;background:var(--footer);color:#ccc}
.footer h4{font-size:15px;font-weight:600;color:var(--white);margin-bottom:14px}
.f-brand{left:176px;top:34px;width:190px}
.f-brand .brand{position:static;align-items:flex-start}
.f-brand .brand-square{background:var(--white);margin-top:4px}
.f-brand .brand-name{color:var(--white);font-size:15px;white-space:normal}
.f-brand p{font-size:10px;line-height:1.6;margin-top:10px;width:170px;color:#aaa}
.f-col{top:34px}
.field{width:170px;height:22px;background:#444;margin-bottom:8px;font-size:10px;color:#999;padding:4px 8px}
.field.tall{height:40px}
.btn-submit{display:inline-block;background:var(--navy);color:var(--white);font-size:10px;font-weight:700;padding:6px 14px}
.contact-row{display:flex;gap:8px;align-items:flex-start;font-size:10px;line-height:1.5;margin-bottom:12px}
.contact-row i{width:10px;height:10px;background:#888;border-radius:50%;margin-top:3px;flex:none}
.squares{display:flex;gap:6px}
.squares span{width:24px;height:24px;display:block}
.bottom{left:0;top:2312px;width:1200px;height:36px;background:var(--footer-deep);font-size:10px;color:#999}
.bottom span{position:absolute;top:11px}
</style>
</head>
<body>

<header class="abs topbar">
  <div class="abs brand"><span class="brand-square"></span><span class="brand-name">Harwick Construction LTD</span></div>
  <div class="abs info" style="left:600px">
    <svg width="16" height="16" viewBox="0 0 16 16"><circle cx="8" cy="8" r="7" fill="none" stroke="#1d2c4c" stroke-width="1.5"/><path d="M8 4v4l3 2" fill="none" stroke="#1d2c4c" stroke-width="1.5"/></svg>
    <span><b>Mon - Sat 8:00 - 17:00</b><br>Sunday closed</span>
  </div>
  <div class="abs info" style="left:780px">
    <svg width="14" height="18" viewBox="0 0 14 18"><path d="M7 1a6 6 0 0 0-6 6c0 4.5 6 10 6 10s6-5.5 6-10a6 6 0 0 0-6-6z" fill="#1d2c4c"/><circle cx="7" cy="7" r="2" fill="#fff"/></svg>
    <span><b>12 Kerrow Lane</b><br>Ashford, Westvale</span>
  </div>
  <div class="abs social"><span></span><span></span><span></span></div>
</header>

<nav class="abs nav">
  <ul><li>HOME</li><li>ABOUT US</li><li>PROJECTS</li><li class="active">SERVICES</li><li>NEWS</li><li>CONTACT US</li></ul>
</nav>
<div class="abs dropdown"><div>Renovations</div><div>Maintenance</div><div>Project Management</div></div>

<section class="abs hero" role="img" aria-label="Bright modern living room interior with large windows">
</section>
<div class="abs hero-box">We do our best so that your house is a place you never want to leave</div>
<div class="abs quote-bar">
  <p>Looking for a quality and affordable construction services for your next project?</p>
  <span class="abs btn-quote">GET A QUOTE &#8250;</span>
</div>

<h2 class="abs section-title" style="left:176px;top:612px">SERVICES</h2>
<div class="abs arrows" style="left:972px;top:616px">
  <span><svg width="8" height="10"><path d="M6 1L2 5l4 4" stroke="#fff" fill="none" stroke-width="2"/></svg></span>
  <span class="on"><svg width="8" height="10"><path d="M2 1l4 4-4 4" stroke="#fff" fill="none" stroke-width="2"/></svg></span>
</div>

<article class="abs card" style="left:176px">
  <div class="img" role="img" aria-label="Builders reviewing plans on a residential site" style="background:linear-gradient(#c8d4e0,#8a96a2)"></div>
  <h3>RESIDENTIAL PROPERTIES</h3>
  <p>Bathrooms, kitchens and alterations carried out by trade qualified builders who treat your home with care from first visit to final handover.</p>
  <div class="read"><i></i>READ MORE</div>
</article>
<article class="abs card" style="left:467px">
  <div class="img" role="img" aria-label="Commercial building under construction" style="background:linear-gradient(#7fa8d4,#b9c6d2)"></div>
  <h3>COMMERCIAL PROPERTIES</h3>
  <p>Shop fit outs and office fit outs planned around your trading hours, delivered on schedule with minimal disruption to staff and customers.</p>
  <div class="read"><i></i>READ MORE</div>
</article>
<article class="abs card" style="left:758px">
  <div class="img" role="img" aria-label="Renovation work on a building exterior" style="background:linear-gradient(#c3ccd4,#9aa28c)"></div>
  <h3>RENOVATIONS</h3>
  <p>We handle every trade from concept to completion, with registered builders managing the project so you get the best possible result.</p>
  <div class="read"><i></i>READ MORE</div>
</article>

<section class="abs featured">
  <h2 class="abs section-title" style="left:176px;top:48px">Featured Projects</h2>
  <div class="abs tabs"><span class="on">ALL PROJECTS</span><span>RESIDENTIAL</span><span>COMMERCIAL</span><span>ALTERATIONS</span><span>COMMERCIAL SHOP</span><span>OFFICE</span></div>
  <div class="abs side-arrow" style="left:104px"><svg width="10" height="14"><path d="M8 2L3 7l5 5" stroke="#fff" fill="none" stroke-width="2"/></svg></div>
  <div class="abs tile" role="img" aria-label="Modern house exterior at dusk" style="left:176px;background:linear-gradient(#3e4a58,#1e252e)">
    <span class="abs tile-label">ALDER RESIDENCE</span>
    <span class="abs tile-btn">VIEW MORE</span>
  </div>
  <div class="abs tile" role="img" aria-label="Renovated kitchen interior" style="left:392px;background:linear-gradient(#a38a6e,#5e4a38)"></div>
  <div class="abs tile" role="img" aria-label="Open plan living space with plants" style="left:608px;background:linear-gradient(#d6d8cf,#9ea692)"></div>
  <div class="abs tile" role="img" aria-label="Contemporary bedroom interior" style="left:824px;background:linear-gradient(#9a7a62,#5a4a3e)"></div>
  <div class="abs side-arrow" style="left:1064px"><svg width="10" height="14"><path d="M2 2l5 5-5 5" stroke="#fff" fill="none" stroke-width="2"/></svg></div>
</section>

<section class="abs mission" role="img" aria-label="Builder in a hard hat against a blue sky">
  <p>We believe in taking care of all manners of trades ranging from concept to completion, along with trade qualified LBP registered builders.</p>
</section>

<h2 class="abs section-title" style="left:176px;top:1712px">Recent News</h2>
<div class="abs arrows" style="left:676px;top:1716px">
  <span><svg width="8" height="10"><path d="M6 1L2 5l4 4" stroke="#fff" fill="none" stroke-width="2"/></svg></span>
  <span class="on"><svg width="8" height="10"><path d="M2 1l4 4-4 4" stroke="#fff" fill="none" stroke-width="2"/></svg></span>
</div>
<article class="abs news" style="left:176px">
  <div class="img" role="img" aria-label="Worker tiling a floor" style="background:linear-gradient(#b8a48e,#6f6254)"></div>
  <p>Our team recently completed a full bathroom and kitchen renovation for a family home, finished two weeks ahead of schedule.</p>
  <div class="news-meta"><span class="btn-dark">View More</span><span class="date">July 12, 2015</span></div>
</article>
<article class="abs news" style="left:468px">
  <div class="img" role="img" aria-label="Builder fitting out an office interior" style="background:linear-gradient(#c9b89c,#7e6a52)"></div>
  <p>A new office fit out for a local firm included open workspaces, meeting rooms and a staff kitchen built around their needs.</p>
  <div class="news-meta"><span class="btn-dark">View More</span><span class="date">July 03, 2015</span></div>
</article>

<h2 class="abs section-title" style="left:768px;top:1712px">Testimonials</h2>
<aside class="abs testi">
  <div class="testi-box">Harwick handled our shop fit out from start to finish. Clear communication, tidy work and a result our customers notice every day.</div>
  <div class="testi-person">
    <div class="avatar" role="img" aria-label="Client portrait"></div>
    <div><b>MARK ELLISON</b><small>Retail Store Owner</small></div>
  </div>
</aside>

<footer class="abs footer">
  <div class="abs f-brand">
    <div class="brand"><span class="brand-square"></span><span class="brand-name">Harwick Construction LTD</span></div>
    <p>Renovation and maintenance specialists for residential and commercial properties.</p>
  </div>
  <div class="abs f-col" style="left:392px">
    <h4>Quick Contact</h4>
    <div class="field">Name</div>
    <div class="field">Email</div>
    <div class="field tall">Message</div>
    <span class="btn-submit">SUBMIT</span>
  </div>
  <div class="abs f-col" style="left:628px">
    <h4>Contact Us</h4>
    <div class="contact-row"><i></i><span>12 Kerrow Lane,<br>Ashford, Westvale</span></div>
    <div class="contact-row"><i></i><span>(555) 014 2290</span></div>
    <div class="contact-row"><i></i><span>info@harwick.example</span></div>
  </div>
  <div class="abs f-col" style="left:832px">
    <h4>Connect Us</h4>
    <div class="squares"><span style="background:#3b5a98"></span><span style="background:#c23a2b"></span><span style="background:#2a8fd0"></span></div>
  </div>
</footer>
<div class="abs bottom">
  <span style="left:176px">&copy; Copyright Harwick Construction LTD</span>
  <span style="left:940px">All rights reserved</span>
</div>

</body>
</html>
```